lifestyle photographer promotion piece

I would like to create a printed postcard to send to potential clients to introduce them to my work and hopefully create new clients. I'm a commercial photographer who just relocated to the Miami area and would really like to be getting more luxury lifestyle and resort work that includes my unique ability to shoot every aspect of lifestyle including food, travel, lifestyle and fashion. I'd like to incorporate between 4-12 of my best images from my online portfolio at www.delphinecarrow.com. The printed piece should also have a very clean, graphic, modern feel to it overall similar to my website. The main goal is to create a striking and compelling grouping of images showing my diverse offerings but in a way that shows an obvious visual style, my style. Please refer to my website for images. When winner is chosen, I will supply hi-res files to compete the design.
Updates

The card is a mailer and a handout. The back of the card should be black and white and text only with my info and an area for address to information. Dimensions of the card are 6x8.5 inches and I prefer the horizontal aspect ratio.

I've noticed a few designers are incorporating graphics. I would like to avoid that. Interested in photography dominated card with /or without graphic use of white space. I tend to avoid color backgrounds, white space is my preference in most cases although I'm not completely against it. 

Target Market(s)

Advertising Agencies and Magazines, Record Labels, Modeling Agencies, Public Relations Firms

Industry/Entity Type

Fashion

Requirements
Must have
• Horizontal

Front(color):
Delphine Carrow Photography
Harbor / Lakeside / Ridgeview

Back(black and white):
(407)614-2958
www.delphinecarrow.com
info@delphinecarrow.com

```html
<!DOCTYPE html>
<html lang="en">
<head>
<meta charset="utf-8">
<title>Delphine Carrow Photography – Postcard Back</title>
<link rel="stylesheet" href="https://fonts.googleapis.com/css2?family=Arimo&family=Archivo:wght@800&display=swap">
<style>
  :root {
    --ink: #000000;
    --paper: #ffffff;
    --zone: #e8e8ea;
    --rule: #8a8a8a;
    --dash: #1a1a1a;
  }
  * { margin: 0; padding: 0; box-sizing: border-box; }
  html, body {
    width: 1200px; height: 852px; overflow: hidden;
    background: var(--paper);
  }
  .postcard {
    position: relative; width: 1200px; height: 852px;
    background: var(--paper); overflow: hidden;
  }
  .trim-frame {
    position: absolute; left: 35px; top: 37px; width: 1131px; height: 782px;
    border: 1px solid var(--rule);
  }
  .zone {
    position: absolute; background: var(--zone);
    font-family: "Archivo", "Arial Black", sans-serif; font-weight: 800;
    font-size: 16px; line-height: 18px; text-align: center;
    color: var(--ink); letter-spacing: 0.6px;
  }
  .zone--indicia { left: 1018px; top: 11px; width: 171px; height: 173px; padding-top: 55px; }
  .zone--address {
    left: 810px; top: 461px; width: 379px; height: 294px; padding-top: 73px;
    border-left: 2px dashed var(--dash);
  }
  .zone--postal {
    left: 218px; top: 755px; width: 971px; height: 88px; padding-top: 35px;
    border-top: 2px dashed var(--dash); border-left: 2px dashed var(--dash);
    text-align: left; padding-left: 452px; letter-spacing: 0.9px;
  }
  .contact-icons {
    position: absolute; left: 41px; top: 57px; width: 43px; height: 119px;
    background: var(--ink);
  }
  .contact-list {
    position: absolute; left: 116px; top: 64px; list-style: none;
    font-family: "Arimo", Arial, sans-serif; font-size: 21px;
    letter-spacing: 2px; color: var(--ink);
  }
  .contact-list li { height: 38.5px; line-height: 28px; }
  .name-band {
    position: absolute; left: 0; top: 203px; width: 1200px; height: 258px;
    background: var(--ink); color: var(--paper); text-align: center;
    font-family: "Arimo", Arial, sans-serif; font-weight: 400;
  }
  .studio-name {
    position: absolute; left: 0; right: 0; top: 72px;
    font-weight: 400; font-size: 52px; line-height: 64px; letter-spacing: 2px;
  }
  .locations {
    position: absolute; left: 0; right: 0; top: 205px;
    font-size: 22px; letter-spacing: 10.5px; line-height: 30px;
  }
</style>
</head>
<body>
<main class="postcard">
  <div class="trim-frame"></div>

  <div class="zone zone--indicia">INDICIA<br>CLEAR<br>ZONE</div>

  <svg class="contact-icons" viewBox="0 0 43 119" aria-hidden="true">
    <g fill="none" stroke="#fff" stroke-width="1.6" stroke-linecap="round" stroke-linejoin="round">
      <path d="M15 8 l4 0 l2 6 l-3 2 q2 5 6 7 l2 -3 l6 2 l0 4 q-1 3 -5 2 q-10 -4 -13 -14 q-1 -5 1 -6 z"/>
      <path d="M23 7 q7 1 8 8"/>
      <path d="M23 11 q3 1 4 4"/>
      <circle cx="21.5" cy="60" r="12"/>
      <ellipse cx="21.5" cy="60" rx="5.5" ry="12"/>
      <line x1="21.5" y1="48" x2="21.5" y2="72"/>
      <line x1="9.5" y1="60" x2="33.5" y2="60"/>
      <path d="M11.5 53 h20 M11.5 67 h20"/>
      <rect x="6" y="89" width="31" height="20"/>
      <path d="M6 89 l15.5 12 l15.5 -12"/>
      <path d="M6 109 l11 -11 M37 109 l-11 -11"/>
    </g>
  </svg>
  <ul class="contact-list">
    <li class="contact-phone">(407)614-2958</li>
    <li class="contact-web">www.delphinecarrow.com</li>
    <li class="contact-email">info@delphinecarrow.com</li>
  </ul>

  <section class="name-band">
    <h1 class="studio-name">Delphine Carrow Photography</h1>
    <p class="locations">Harbor / Lakeside / Ridgeview</p>
  </section>

  <div class="zone zone--address">MAILING ADDRESS<br>ONLY</div>
  <div class="zone zone--postal">BARCODE &amp; POSTAL MARKINGS AREA</div>
</main>
</body>
</html>
```